Brevard Consulting Stationary and Business Card
Professional Modern Stationary and Business Card Design
Brevard Consulting Stationary and Business Card -
Creative Brief
Bright & Fun-filled
Owen P. Marsh
Consultant
517 Alder Lane New City, NY 10948
owen@pelmarconsult.example
www.pelmarconsult.example
I am looking for professional business cards to be provided to educators so that they remember me and my business. I am hoping the stationary will carry the look and feel of the business card. The stationary can be simple in design but professional. Text needs to be easily modifiable in design.
I am looking to be able to add bullet points to the back of the business card. I am expecting to have 3 to 5 bullets such as: * Technology Plan Creation * Education Technology Support * Teacher Professional Development * Budgeting * IT Support to help with business processes

```html
<!DOCTYPE html>
<html lang="en">
<head>
<meta charset="utf-8">
<title>Brevard Consulting Stationery Concept</title>
<link rel="stylesheet" href="https://fonts.googleapis.com/css2?family=Open+Sans:wght@400;600;700;800&display=swap">
<style>
  :root {
    --board: #2b2b2d;
    --board-edge: #1c1c1e;
    --paper: #ffffff;
    --blue: #1b6fc2;
    --blue-deep: #0f4f93;
    --green: #7cc242;
    --green-light: #a6d86a;
    --ink: #4a4a4a;
    --muted: #8a8a8a;
    --label: #c9c9c9;
  }
  * { box-sizing: border-box; margin: 0; padding: 0; }
  html, body { width: 1200px; height: 598px; overflow: hidden; }
  body {
    background: radial-gradient(ellipse at 60% 40%, var(--board) 0%, var(--board-edge) 100%);
    font-family: "Open Sans", Arial, sans-serif;
    color: var(--ink);
    position: relative;
  }
  .piece { position: absolute; background: var(--paper); overflow: hidden; box-shadow: 0 3px 10px rgba(0,0,0,.5); }
  .swoosh { position: absolute; inset: 0; width: 100%; height: 100%; }
  .caption { position: absolute; font-size: 9px; color: var(--label); text-align: center; }

  .brand { position: absolute; display: flex; align-items: center; gap: 5px; }
  .brand-dot { border-radius: 50%; background: var(--green); flex: none; }
  .brand-name { font-weight: 800; color: var(--blue); letter-spacing: .5px; line-height: 1; }

  /* business cards */
  .card { width: 228px; height: 132px; left: 36px; }
  .card-front { top: 130px; }
  .card-back-one { top: 319px; }
  .card-back-two { top: 480px; height: 92px; }
  .card .brand { left: 50%; transform: translateX(-50%); top: 14px; }
  .card .brand-dot { width: 14px; height: 14px; }
  .card .brand-name { font-size: 20px; }
  .card-front .brand { top: 12px; }
  .holder { position: absolute; left: 16px; top: 50px; }
  .holder-name { font-size: 10px; font-weight: 700; color: var(--blue); line-height: 1.3; }
  .holder-role { font-size: 6px; color: var(--muted); margin-bottom: 4px; }
  .small { font-size: 5px; line-height: 1.5; color: var(--ink); }
  .contact { position: absolute; left: 118px; top: 52px; }
  .services { position: absolute; list-style: none; font-size: 6px; line-height: 1.6; color: var(--ink); white-space: nowrap; }
  .services li::before { content: "\2713  "; color: var(--green); font-weight: 700; }
  .card-back-one .services { left: 34px; top: 56px; }
  .card-back-two .brand { left: 10px; top: 32px; transform: none; }
  .card-back-two .brand-name { font-size: 13px; }
  .card-back-two .brand-dot { width: 10px; height: 10px; }
  .card-back-two .services { left: 92px; top: 14px; font-size: 5.5px; line-height: 1.55; }

  /* letterhead */
  .letterhead { left: 300px; top: 48px; width: 372px; height: 511px; }
  .letterhead .brand { left: 28px; top: 26px; }
  .letterhead .brand-dot { width: 18px; height: 18px; }
  .letterhead .brand-name { font-size: 26px; }
  .letterhead .sender { position: absolute; left: 240px; top: 22px; }

  /* logo showcase */
  .showcase .brand { left: 800px; top: 104px; }
  .showcase .brand-dot { width: 40px; height: 40px; }
  .showcase .brand-name { font-size: 54px; color: var(--blue); }
  .showcase-rule { position: absolute; left: 850px; top: 170px; width: 300px; height: 3px; background: linear-gradient(90deg, var(--green), var(--blue)); }
  .showcase-title { position: absolute; left: 850px; top: 182px; font-size: 14px; color: var(--label); }

  /* envelope */
  .envelope { left: 732px; top: 384px; width: 432px; height: 175px; }
  .envelope .brand { left: 36px; top: 26px; }
  .envelope .brand-dot { width: 16px; height: 16px; }
  .envelope .brand-name { font-size: 22px; }
  .envelope .return { position: absolute; left: 54px; top: 56px; }
</style>
</head>
<body>

  <!-- Front business card -->
  <section class="piece card card-front">
    <svg class="swoosh" viewBox="0 0 228 132" preserveAspectRatio="none" aria-hidden="true">
      <path d="M0 118 Q80 134 228 110 L228 132 L0 132Z" fill="var(--blue)"/>
      <path d="M0 112 Q80 128 228 104 L228 108 Q80 132 0 116Z" fill="var(--green)"/>
    </svg>
    <div class="brand"><span class="brand-dot"></span><span class="brand-name">Brevard</span></div>
    <div class="holder">
      <p class="holder-name">Owen P. Marsh</p>
      <p class="holder-role">Consultant</p>
      <p class="small">517 Alder Lane<br>New City, NY 10948</p>
    </div>
    <div class="contact small">
      <p>(845) 555-0142</p>
      <p>(845) 555-0199</p>
      <p>owen@pelmarconsult.example</p>
      <p>www.pelmarconsult.example</p>
    </div>
  </section>
  <p class="caption" style="left:36px;top:268px;width:228px;">Front Card</p>

  <!-- Back card option 1 -->
  <section class="piece card card-back-one">
    <svg class="swoosh" viewBox="0 0 228 132" preserveAspectRatio="none" aria-hidden="true">
      <path d="M0 0 L228 0 L228 10 Q120 4 0 22Z" fill="var(--blue)"/>
      <path d="M0 104 Q60 124 228 114 L228 132 L0 132Z" fill="var(--green)"/>
    </svg>
    <div class="brand" style="top:24px;"><span class="brand-dot"></span><span class="brand-name">Brevard</span></div>
    <ul class="services">
      <li>Technology Plan Creation</li>
      <li>Education Technology Support</li>
      <li>Teacher Professional Development</li>
      <li>Budgeting</li>
      <li>IT Support to help with business processes</li>
    </ul>
  </section>
  <p class="caption" style="left:36px;top:455px;width:228px;">Back Card Option1</p>

  <!-- Back card option 2 -->
  <section class="piece card card-back-two">
    <svg class="swoosh" viewBox="0 0 228 92" preserveAspectRatio="none" aria-hidden="true">
      <path d="M0 0 L228 0 L228 6 Q110 2 0 14Z" fill="var(--green)"/>
      <path d="M0 80 Q80 94 228 84 L228 92 L0 92Z" fill="var(--blue)"/>
    </svg>
    <div class="brand"><span class="brand-dot"></span><span class="brand-name">Brevard</span></div>
    <ul class="services">
      <li>Technology Plan Creation</li>
      <li>Education Technology Support</li>
      <li>Teacher Professional Development</li>
      <li>Budgeting</li>
      <li>IT Support to help with business processes</li>
    </ul>
  </section>
  <p class="caption" style="left:36px;top:578px;width:228px;">Back Card Option2</p>

  <!-- Letterhead -->
  <section class="piece letterhead">
    <svg class="swoosh" viewBox="0 0 372 511" preserveAspectRatio="none" aria-hidden="true">
      <path d="M0 0 L22 0 Q8 80 0 120Z" fill="var(--green)"/>
      <path d="M372 430 Q300 500 200 511 L372 511Z" fill="var(--blue)"/>
      <path d="M372 452 Q320 500 250 511 L272 511 Q330 498 372 466Z" fill="var(--green-light)"/>
    </svg>
    <div class="brand"><span class="brand-dot"></span><span class="brand-name">Brevard</span></div>
    <div class="sender small">
      <p>517 Alder Lane</p>
      <p>New City, NY 10948</p>
      <p>(845) 555-0142</p>
      <p>(845) 555-0199</p>
      <p>owen@pelmarconsult.example</p>
      <p>www.pelmarconsult.example</p>
    </div>
  </section>
  <p class="caption" style="left:300px;top:566px;width:372px;">Letter head</p>

  <!-- Logo showcase -->
  <div class="showcase">
    <div class="brand"><span class="brand-dot"></span><span class="brand-name">Brevard</span></div>
    <div class="showcase-rule"></div>
    <p class="showcase-title">Stationary Concept</p>
  </div>

  <!-- Envelope -->
  <section class="piece envelope">
    <svg class="swoosh" viewBox="0 0 432 175" preserveAspectRatio="none" aria-hidden="true">
      <path d="M0 0 L26 0 Q14 90 0 175Z" fill="var(--blue)"/>
      <path d="M26 0 L34 0 Q20 90 0 175 L0 160 Q14 80 26 0Z" fill="var(--green)"/>
      <path d="M432 0 L432 30 Q410 10 370 0Z" fill="var(--blue-deep)"/>
    </svg>
    <div class="brand"><span class="brand-dot"></span><span class="brand-name">Brevard</span></div>
    <p class="return small">517 Alder Lane New City, NY 10948</p>
  </section>
  <p class="caption" style="left:732px;top:566px;width:432px;">Envelope</p>

</body>
</html>
```